Pinecrest Artisan League Membership

UPDATED files - 06/03/2021
Digital brochure needed for construction contractor related nonprofit organization.
Document will be primarily for digital viewing with potential for print version. Should be branded with our branding (logo attached). This is intended to be a multiple page document, plan to print and web (email) use. Standard Letter size document 8.5 x 11 inch
Portrait format preferred
The attached project brief includes a cover, 4 internal pages, and a back cover. This is flexible pending design layout
Target Market(s)
Residential construction business owners
Requirements
Must have
- See attached brief.Orange color palette: RGB: (253,153,0)
Nice to have
- See attached bief
Should not have
- No suit or ties. button up shirt okay, but not white collar worker.

```html
<!DOCTYPE html>
<html lang="en">
<head>
<meta charset="utf-8">
<title>Pinecrest Artisan League — Membership Brochure</title>
<link rel="stylesheet" href="https://fonts.googleapis.com/css2?family=Montserrat:wght@500;600;800&family=Open+Sans:wght@400;600&display=swap">
<style>
:root{
  --board:#f7d789;
  --orange:#fd9900;
  --orange-soft:#fbb54a;
  --ink:#1c1c1c;
  --body:#3a3a3a;
  --rule:#5a5a5a;
  --paper:#ffffff;
  --black:#0d0d0d;
}
*{margin:0;padding:0;box-sizing:border-box}
html,body{width:783px;height:1200px;overflow:hidden;background:var(--board)}
body{position:relative;font-family:"Open Sans",Arial,sans-serif;color:var(--body)}
.page{position:absolute;width:343px;height:266px;background:var(--paper);overflow:hidden}
.col-l{left:31px}.col-r{left:406px}
.row-1{top:31px}.row-2{top:322px}.row-3{top:614px}.row-4{top:906px}

.photo-col{position:absolute;left:0;top:0;width:146px;height:100%}
.tone-warm{background:linear-gradient(180deg,#c9b9a2 0%,#d8b58a 35%,#f3a43a 70%,var(--orange) 100%)}
.tone-green{background:linear-gradient(180deg,#b9c59a 0%,#d6c29c 35%,#f3a640 68%,var(--orange) 100%)}
.tone-desk{background:linear-gradient(180deg,#7f8a6a 0%,#efe3cf 30%,#f7c98c 60%,var(--orange) 100%)}
.tone-site{background:linear-gradient(180deg,#c7a77e 0%,#d8c3a1 35%,#f2aa4c 68%,var(--orange) 100%)}
.tone-sky{background:linear-gradient(180deg,#e9e4d6 0%,#d9b98a 35%,#f3a640 68%,var(--orange) 100%)}
.tone-night{background:linear-gradient(180deg,#6a6658 0%,#c7a66d 35%,#f2aa4c 68%,var(--orange) 100%)}

.copy{position:absolute;left:160px;top:15px;width:168px}
.copy h2{font-family:"Montserrat",Arial,sans-serif;font-weight:600;font-size:12.5px;line-height:1.05;color:var(--ink);padding-bottom:2px;border-bottom:.6px solid var(--rule);margin-bottom:6px;width:150px}
.copy h2.wide{width:170px}
.copy h3{font-family:"Open Sans",Arial,sans-serif;font-weight:600;font-size:5.6px;color:var(--ink);margin-top:1px}
.copy p{font-size:4.5px;line-height:1.3;margin-bottom:5px}
.copy .gap{margin-top:9px}
.dots{list-style:none;font-size:4.5px;line-height:1.75;margin-bottom:7px}
.dots li{position:relative;padding-left:7px}
.dots li::before{content:"";position:absolute;left:0;top:2.4px;width:2.4px;height:2.4px;border-radius:50%;background:var(--orange)}
.dots.two{display:grid;grid-template-columns:73px 1fr;margin-left:1px}
.dots.tight{line-height:1.35}
.dots.tight li{margin-bottom:2px}

.values{list-style:none;margin-left:12px;font-size:4.5px;line-height:1.3}
.values li{display:flex;align-items:flex-start;gap:6px;min-height:12px;margin-bottom:3px}
.values svg{flex:none;width:8px;height:8px;margin-top:-1px}

.foot{position:absolute;bottom:8px;left:0;width:100%;height:6px;font-size:3.3px;color:var(--ink)}
.foot span{position:absolute;display:flex;align-items:center;gap:2px;white-space:nowrap}
.foot svg{width:4px;height:4px}
.foot .mail{left:102px;color:#fff}
.foot .tel{left:150px}
.foot .web{left:185px}
.foot .mark{left:275px;font-family:"Montserrat",Arial,sans-serif;font-weight:800;font-size:3.6px;color:var(--ink)}

/* cover */
.cover .bar-top{position:absolute;top:0;left:0;width:100%;height:15px;background:linear-gradient(90deg,var(--black) 0 65px,var(--orange) 65px)}
.cover .hero{position:absolute;top:15px;left:0;width:100%;height:175px;background:linear-gradient(90deg,#b9b0a0 0%,#d3b07a 40%,#f7b14d 70%,var(--orange) 100%)}
.cover .bar-bot{position:absolute;top:190px;left:0;width:100%;height:13px;background:linear-gradient(90deg,var(--black) 0 65px,var(--orange) 65px)}
.brand-lg{position:absolute;top:220px;left:0;width:100%;text-align:center;font-family:"Montserrat",Arial,sans-serif;font-weight:800;font-size:15px;letter-spacing:-.3px;color:var(--ink)}

/* back cover */
.back .bar-top{position:absolute;top:0;left:0;width:100%;height:15px;background:linear-gradient(90deg,var(--orange) 0 53px,var(--black) 100px)}
.back .hero{position:absolute;top:15px;left:0;width:100%;height:175px;background:linear-gradient(90deg,var(--orange) 0%,#e3b680 25%,#c8c4bb 55%,#dfe7f0 100%)}
.back .bar-bot{position:absolute;top:190px;left:0;width:100%;height:12px;background:linear-gradient(90deg,var(--orange) 0 53px,var(--black) 53px)}
.back .rule{position:absolute;bottom:6px;left:0;width:100%;height:1.5px;background:linear-gradient(90deg,var(--orange) 0 53px,var(--black) 53px)}
.brand-md{position:absolute;top:218px;left:62px;width:92px;font-family:"Montserrat",Arial,sans-serif;font-weight:800;font-size:11px;line-height:1.05;color:var(--ink)}
.contact-list{position:absolute;top:215px;left:188px;list-style:none;font-size:6.3px;line-height:1.6;color:var(--ink)}
.contact-list li{display:flex;align-items:center;gap:4px}
.contact-list svg{width:6px;height:6px}
</style>
</head>
<body>

<!-- Cover -->
<section class="page cover col-l row-1">
  <div class="bar-top"></div>
  <div class="hero" role="img" aria-label="Photo of two contractors in hard hats and safety vests reviewing plans on a tablet, fading into orange"></div>
  <div class="bar-bot"></div>
  <div class="brand-lg">Pinecrest Artisan League</div>
</section>

<!-- Mission / Vision / Values -->
<section class="page col-r row-1">
  <div class="photo-col tone-warm" role="img" aria-label="Portrait of a contractor in a yellow hard hat and orange vest, fading into orange"></div>
  <div class="copy">
    <h2>Mission</h2>
    <p>To promote, educate and advance a diverse contractor community by providing pathways of accessibility to help build a stronger foundation for a better future.</p>
    <h2 class="gap">Vision</h2>
    <p>To become the preferred organization for construction contractors striving to be the best in their trade through education, training, and ongoing development.</p>
    <h2 class="gap">Core Values</h2>
    <ul class="values">
      <li><svg viewBox="0 0 10 10"><circle cx="5" cy="5" r="4.2" fill="none" stroke="#fd9900" stroke-width=".9"/><path d="M3 5.2l1.5 1.5L8.6 2.2" fill="none" stroke="#fd9900" stroke-width="1"/></svg>Empower through learning &amp; development</li>
      <li><svg viewBox="0 0 10 10"><circle cx="5" cy="5" r="4.2" fill="none" stroke="#fd9900" stroke-width=".9"/><path d="M3 5.2l1.5 1.5L8.6 2.2" fill="none" stroke="#fd9900" stroke-width="1"/></svg>Strengthen &amp; sustain the industry</li>
      <li><svg viewBox="0 0 10 10"><circle cx="5" cy="5" r="4.2" fill="none" stroke="#fd9900" stroke-width=".9"/><path d="M3 5.2l1.5 1.5L8.6 2.2" fill="none" stroke="#fd9900" stroke-width="1"/></svg>Build partnerships to benefit underserved<br>communities</li>
      <li><svg viewBox="0 0 10 10"><circle cx="5" cy="5" r="4.2" fill="none" stroke="#fd9900" stroke-width=".9"/><path d="M3 5.2l1.5 1.5L8.6 2.2" fill="none" stroke="#fd9900" stroke-width="1"/></svg>Act with integrity, respect, and honesty</li>
      <li><svg viewBox="0 0 10 10"><circle cx="5" cy="5" r="4.2" fill="none" stroke="#fd9900" stroke-width=".9"/><path d="M3 5.2l1.5 1.5L8.6 2.2" fill="none" stroke="#fd9900" stroke-width="1"/></svg>Promote diversity, equity, and inclusion<br>throughout the industry</li>
    </ul>
  </div>
  <div class="foot">
    <span class="mail"><svg viewBox="0 0 10 10"><rect x="1" y="2.5" width="8" height="5" fill="none" stroke="currentColor"/><path d="M1 2.5l4 3 4-3" fill="none" stroke="currentColor"/></svg>hello@pinecrestleague.org</span>
    <span class="tel"><svg viewBox="0 0 10 10"><circle cx="5" cy="5" r="4" fill="none" stroke="currentColor"/><path d="M3.5 3l1 1-.6.8 1.4 1.4.8-.6 1 1-.8.8C4.8 7.2 2.8 5.2 2.7 3.8z" fill="currentColor"/></svg>555-014-2290</span>
    <span class="web"><svg viewBox="0 0 10 10"><circle cx="5" cy="5" r="4" fill="none" stroke="currentColor"/><path d="M1 5h8M5 1c-2 2.5-2 5.5 0 8M5 1c2 2.5 2 5.5 0 8" fill="none" stroke="currentColor" stroke-width=".7"/></svg>pinecrestleague.org</span>
    <span class="mark">Pinecrest Artisan League</span>
  </div>
</section>

<!-- DEI / About -->
<section class="page col-l row-2">
  <div class="photo-col tone-green" role="img" aria-label="Photo of two builders on a site, one pointing up and one holding a binder, fading into orange"></div>
  <div class="copy">
    <h2>Diversity, Equity &amp;<br>Inclusion</h2>
    <p>PAL promotes and encourages open dialogue and positive working environments for BIPOC and other identity groups, to thrive within a contractor community and facilitate a more inclusive and resilient future.</p>
    <h2 class="gap">About Us</h2>
    <p>PAL was founded in 2014 as a resource for construction business owners. Since inception, we've been working with contractors on a daily basis allowing us to better understand the many challenges construction contractors face. Seeing these challenges firsthand propelled us to empower our members to implement sound business practices and safety protocols that will allow their business to strengthen, grow, and expand.</p>
    <p>Our goal is to create a community of contractors who are better prepared to overcome challenges within the industry, empowering them to share ideas, lessons learned, proven practices, and insights with other industry leaders.</p>
  </div>
  <div class="foot">
    <span class="mail"><svg viewBox="0 0 10 10"><rect x="1" y="2.5" width="8" height="5" fill="none" stroke="currentColor"/><path d="M1 2.5l4 3 4-3" fill="none" stroke="currentColor"/></svg>hello@pinecrestleague.org</span>
    <span class="tel"><svg viewBox="0 0 10 10"><circle cx="5" cy="5" r="4" fill="none" stroke="currentColor"/><path d="M3.5 3l1 1-.6.8 1.4 1.4.8-.6 1 1-.8.8C4.8 7.2 2.8 5.2 2.7 3.8z" fill="currentColor"/></svg>555-014-2290</span>
    <span class="web"><svg viewBox="0 0 10 10"><circle cx="5" cy="5" r="4" fill="none" stroke="currentColor"/><path d="M1 5h8M5 1c-2 2.5-2 5.5 0 8M5 1c2 2.5 2 5.5 0 8" fill="none" stroke="currentColor" stroke-width=".7"/></svg>pinecrestleague.org</span>
    <span class="mark">Pinecrest Artisan League</span>
  </div>
</section>

<!-- Technical Assistance -->
<section class="page col-r row-2">
  <div class="photo-col tone-desk" role="img" aria-label="Photo of a desk with a laptop keyboard, notebook, pencil, phone and a small plant, fading into orange"></div>
  <div class="copy">
    <h2>Technical Assistance</h2>
    <p>One of our primary goals is to provide technical assistance to the contractor community based on individual level of competency. We understand that the needs of contractors vary greatly based on experience, training, past mentorship.</p>
    <p>Technical assistance takes many forms including business formation assistance, contractor licensing (OR, WA), insurance consulting, access to legal resources as well as assistance with government program funding (PPP Loans, business grants, scholarships), and various networking opportunities.</p>
    <p>Pinecrest Artisan League provides technical assistance in one-on-one consulting as well as group coaching and continuing guidance.</p>
  </div>
  <div class="foot">
    <span class="mail"><svg viewBox="0 0 10 10"><rect x="1" y="2.5" width="8" height="5" fill="none" stroke="currentColor"/><path d="M1 2.5l4 3 4-3" fill="none" stroke="currentColor"/></svg>hello@pinecrestleague.org</span>
    <span class="tel"><svg viewBox="0 0 10 10"><circle cx="5" cy="5" r="4" fill="none" stroke="currentColor"/><path d="M3.5 3l1 1-.6.8 1.4 1.4.8-.6 1 1-.8.8C4.8 7.2 2.8 5.2 2.7 3.8z" fill="currentColor"/></svg>555-014-2290</span>
    <span class="web"><svg viewBox="0 0 10 10"><circle cx="5" cy="5" r="4" fill="none" stroke="currentColor"/><path d="M1 5h8M5 1c-2 2.5-2 5.5 0 8M5 1c2 2.5 2 5.5 0 8" fill="none" stroke="currentColor" stroke-width=".7"/></svg>pinecrestleague.org</span>
    <span class="mark">Pinecrest Artisan League</span>
  </div>
</section>

<!-- Safety & Compliance -->
<section class="page col-l row-3">
  <div class="photo-col tone-site" role="img" aria-label="Photo of a crew in hard hats and vests under timber roof framing, fading into orange"></div>
  <div class="copy">
    <h2>Safety &amp; Compliance</h2>
    <h3>SiteLogbook</h3>
    <p>Sitelogbook.com is a secure, web-based application that enables employers to create each state's first report of injury, track injuries, print all required OSHA reports, and view injury metrics in real-time.</p>
    <p>Automatically generate PDF versions of documents to print, share, or email.</p>
    <p>Works with all devices: computers, tablets, and smartphones. Once data is entered and intuitively updated on all other forms, SiteLogbook will automatically generate benchmark figures with no additional input by location and log.</p>
    <h3>CrewGuard</h3>
    <p>Pinecrest Artisan League has partnered with CrewGuard to give you just the tools you need to protect your workers, meet compliance requirements, and create a positive workspace environment for your employees and others you may work with. CrewGuard's staff of safety professionals, safety trainers, and administrative staff combined with innovative technology has helped thousands of contractors across the nation save money and improve efficiency.</p>
    <p>Included in the mobile app are the following:</p>
    <ul class="dots tight">
      <li>Over 900 bilingual safety lesson topics with digital signoff rosters</li>
      <li>An online form builder to create job and equipment-specific inspection forms</li>
      <li>Mobile-accessible document storage repository</li>
      <li>Training webinars on-the-go, ready to watch when you have time</li>
    </ul>
  </div>
  <div class="foot">
    <span class="mail"><svg viewBox="0 0 10 10"><rect x="1" y="2.5" width="8" height="5" fill="none" stroke="currentColor"/><path d="M1 2.5l4 3 4-3" fill="none" stroke="currentColor"/></svg>hello@pinecrestleague.org</span>
    <span class="tel"><svg viewBox="0 0 10 10"><circle cx="5" cy="5" r="4" fill="none" stroke="currentColor"/><path d="M3.5 3l1 1-.6.8 1.4 1.4.8-.6 1 1-.8.8C4.8 7.2 2.8 5.2 2.7 3.8z" fill="currentColor"/></svg>555-014-2290</span>
    <span class="web"><svg viewBox="0 0 10 10"><circle cx="5" cy="5" r="4" fill="none" stroke="currentColor"/><path d="M1 5h8M5 1c-2 2.5-2 5.5 0 8M5 1c2 2.5 2 5.5 0 8" fill="none" stroke="currentColor" stroke-width=".7"/></svg>pinecrestleague.org</span>
    <span class="mark">Pinecrest Artisan League</span>
  </div>
</section>

<!-- Contractor Education -->
<section class="page col-r row-3">
  <div class="photo-col tone-sky" role="img" aria-label="Photo of two builders in yellow hard hats working together outdoors, fading into orange"></div>
  <div class="copy">
    <h2 class="wide">Contractor Education</h2>
    <p>PAL provides education through live classes, training workshops, and via eLearning courses. We provide in-class training for EPA/RRP Certification, CPR/First Aid certification, and Fall Protection certification.</p>
    <p>We also offer a full suite of online construction education courses to help contractors learn at their own pace without having to travel and at the times available outside regular business hours. Online courses include:</p>
    <ul class="dots two">
      <li>OSHA 10 &amp; 30 training</li><li>HAZWOPER</li>
      <li>Trade-specific skills</li><li>Construction management</li>
      <li>Safety courses</li><li>Environmental exposure</li>
      <li>Administrative courses</li><li>And much more...</li>
    </ul>
    <p class="gap">We also offer targeted training tracks in specific skillsets to promote business development necessary to operate an efficient business. Skillsets include:</p>
    <ul class="dots two">
      <li>Business operations</li><li>Safety &amp; Compliance training</li>
      <li>Business Law &amp; Contracts</li><li>Marketing &amp; Networking</li>
      <li>Financial intelligence</li><li>Business Technology</li>
    </ul>
  </div>
  <div class="foot">
    <span class="mail"><svg viewBox="0 0 10 10"><rect x="1" y="2.5" width="8" height="5" fill="none" stroke="currentColor"/><path d="M1 2.5l4 3 4-3" fill="none" stroke="currentColor"/></svg>hello@pinecrestleague.org</span>
    <span class="tel"><svg viewBox="0 0 10 10"><circle cx="5" cy="5" r="4" fill="none" stroke="currentColor"/><path d="M3.5 3l1 1-.6.8 1.4 1.4.8-.6 1 1-.8.8C4.8 7.2 2.8 5.2 2.7 3.8z" fill="currentColor"/></svg>555-014-2290</span>
    <span class="web"><svg viewBox="0 0 10 10"><circle cx="5" cy="5" r="4" fill="none" stroke="currentColor"/><path d="M1 5h8M5 1c-2 2.5-2 5.5 0 8M5 1c2 2.5 2 5.5 0 8" fill="none" stroke="currentColor" stroke-width=".7"/></svg>pinecrestleague.org</span>
    <span class="mark">Pinecrest Artisan League</span>
  </div>
</section>

<!-- Directory -->
<section class="page col-l row-4">
  <div class="photo-col tone-night" role="img" aria-label="Photo of two workers in white hard hats and reflective jackets checking a device, fading into orange"></div>
  <div class="copy" style="left:157px;width:175px">
    <h2 class="wide" style="width:172px">Directory for Contractors</h2>
    <p>BuilderFinder.com is a FREE effortless way for contractors to connect with property owners to search for a contractor in their local area. As marketing has evolved, contractors need to adopt a variety of online tools and technologies to help gain more online visibility which will result in more business for you.</p>
    <p>The site gives instant access to residential and commercial contractors, an online bid request system, links to the contractor's social media pages and a review system all in one spot.</p>
    <p>Create your business profile and easily manage your unlimited FREE Bid requests, reviews, social media, photo gallery, VidStream videos just to name a few. Having a profile listing adds legitimacy to your business.</p>
    <p>A prime advantage of having your business listed is the SEO and relevant incoming "links to your business". Link building is an important building block of any SEO campaign.</p>
  </div>
  <div class="foot">
    <span class="mail"><svg viewBox="0 0 10 10"><rect x="1" y="2.5" width="8" height="5" fill="none" stroke="currentColor"/><path d="M1 2.5l4 3 4-3" fill="none" stroke="currentColor"/></svg>hello@pinecrestleague.org</span>
    <span class="tel"><svg viewBox="0 0 10 10"><circle cx="5" cy="5" r="4" fill="none" stroke="currentColor"/><path d="M3.5 3l1 1-.6.8 1.4 1.4.8-.6 1 1-.8.8C4.8 7.2 2.8 5.2 2.7 3.8z" fill="currentColor"/></svg>555-014-2290</span>
    <span class="web"><svg viewBox="0 0 10 10"><circle cx="5" cy="5" r="4" fill="none" stroke="currentColor"/><path d="M1 5h8M5 1c-2 2.5-2 5.5 0 8M5 1c2 2.5 2 5.5 0 8" fill="none" stroke="currentColor" stroke-width=".7"/></svg>pinecrestleague.org</span>
    <span class="mark">Pinecrest Artisan League</span>
  </div>
</section>

<!-- Back cover -->
<section class="page back col-r row-4">
  <div class="bar-top"></div>
  <div class="hero" role="img" aria-label="Image of a miniature house under construction with tiny builders on rolled blueprints, fading into orange at the left"></div>
  <div class="bar-bot"></div>
  <div class="brand-md">Pinecrest Artisan League</div>
  <ul class="contact-list">
    <li><svg viewBox="0 0 10 10"><circle cx="5" cy="5" r="4" fill="none" stroke="#fd9900"/><path d="M3.5 3l1 1-.6.8 1.4 1.4.8-.6 1 1-.8.8C4.8 7.2 2.8 5.2 2.7 3.8z" fill="#fd9900"/></svg>555-014-2290</li>
    <li><svg viewBox="0 0 10 10"><rect x="1" y="2.5" width="8" height="5" fill="none" stroke="#fd9900"/><path d="M1 2.5l4 3 4-3" fill="none" stroke="#fd9900"/></svg>hello@pinecrestleague.org</li>
    <li><svg viewBox="0 0 10 10"><circle cx="5" cy="5" r="4" fill="none" stroke="#fd9900"/><path d="M1 5h8M5 1c-2 2.5-2 5.5 0 8M5 1c2 2.5 2 5.5 0 8" fill="none" stroke="#fd9900" stroke-width=".7"/></svg>pinecrestleague.org</li>
  </ul>
  <div class="rule"></div>
</section>

</body>
</html>
```